The tide parlor saltwater aquarium store business card

Looking for a serious business card for a saltwater fish and coral store. I want this thing to blow people's minds when they see it. I would like the card to look very professional but I also want people to know what the tide parlor is just by seeing the card. Iam pretty open to anything as long as it's one of a kind.

Industry/Entity Type

Business

Contact Information for Business Card

18635 Walden highway Brackton pa 15872. Thetideparlor.example. Customerservice@thetideparlor.example. 7245550148

Requirements
Should not have
• Please no child like fish designs

```html
<!DOCTYPE html>
<html lang="en">
<head>
<meta charset="utf-8">
<title>The Tide Parlor – Business Card</title>
<link rel="stylesheet" href="https://fonts.googleapis.com/css2?family=Source+Sans+3:wght@400;600&display=swap">
<style>
  :root {
    --stage: #3a332e;
    --card: #141414;
    --card-edge: #1c1c1c;
    --accent: #1f86d6;
    --accent-soft: #4a90d6;
    --ink: #f2f2f2;
    --swirl: #232629;
  }
  * { box-sizing: border-box; margin: 0; padding: 0; }
  html, body {
    width: 1200px; height: 844px; overflow: hidden;
    background: var(--stage);
    font-family: "Source Sans 3", "Myriad Pro", sans-serif;
  }
  .stage {
    position: relative; width: 1200px; height: 844px;
  }
  .card {
    position: absolute; width: 520px; height: 300px;
    background: var(--card);
    box-shadow: 0 14px 30px rgba(0,0,0,.45);
    overflow: hidden;
  }
  /* back side: contact details */
  .card--back { left: 50px; top: 272px; }
  .card--back .band {
    position: absolute; left: 0; width: 100%; height: 14px;
    background: var(--accent);
  }
  .card--back .band--top { top: 0; }
  .card--back .band--bottom { bottom: 0; }
  .card--back .wave-mark {
    position: absolute; left: 40px; top: 14px; width: 300px; height: 272px;
    background: radial-gradient(ellipse at 55% 45%, var(--swirl) 0%, rgba(35,38,41,.5) 45%, transparent 72%);
  }
  .contact {
    position: absolute; left: 170px; top: 62px; width: 300px;
    color: var(--ink); font-size: 17px; line-height: 1.3;
    text-align: center;
  }
  .contact .address { margin-bottom: 44px; text-align: left; padding-left: 8px; }
  /* front side: name */
  .card--front { left: 630px; top: 272px; background: linear-gradient(160deg, var(--card-edge), var(--card)); }
  .card--front .tab {
    position: absolute; width: 22px; height: 44px;
    background: var(--accent-soft);
    border-right: 3px solid #d8d8d8;
  }
  .card--front .tab--left { left: 0; top: 146px; }
  .card--front .tab--right { right: 0; top: 24px; border-right: none; border-left: 3px solid #d8d8d8; }
  .brand {
    position: absolute; left: 0; right: 0; top: 118px;
    display: flex; align-items: center; justify-content: center; gap: 14px;
  }
  .brand .dot {
    width: 26px; height: 26px; border-radius: 50%; background: var(--accent);
  }
  .brand .name {
    color: var(--ink); font-size: 42px; font-weight: 600; letter-spacing: .5px;
  }
</style>
</head>
<body>
<main class="stage">
  <section class="card card--back" aria-label="Card back with contact details">
    <div class="band band--top"></div>
    <div class="wave-mark" role="img" aria-label="Faint wave emblem decoration"></div>
    <div class="contact">
      <p class="address">18635 Walden highway<br>Brackton pa 15872.</p>
      <p>7245550148</p>
      <p>customerservice@thetideparlor.example</p>
      <p>www.thetideparlor.example.</p>
    </div>
    <div class="band band--bottom"></div>
  </section>

  <section class="card card--front" aria-label="Card front with business name">
    <div class="tab tab--right"></div>
    <div class="tab tab--left"></div>
    <div class="brand">
      <span class="dot"></span>
      <span class="name">The Tide Parlor</span>
    </div>
  </section>
</main>
</body>
</html>
```